WeatheredIt.net wordpress design

Concept: Website where personal stories, personal videos can be posted as a challenge while awaiting the wisdom of experience from others who have survived this same event or challenge in their lifetime.
Support aspects will be in 4 quadrants of Challenges:
1. Financial 2. Medical & Physical
3. Legal Matters 4. Psychological & Spiritual - ability to chat online with a spiritual/psychological counselor or life coach
Updates
Wanted to thank all of you for your designs! Greatly appreciated. Very creative ideas that captured the essence of this website. Will be back with a selection very shortly.
Target Market(s)
Anyone looking for a solution based upon experiential wisdom
Industry/Entity Type
Financial
Requirements
Must have
- Interactive website: Where you can post a challenge or issue via a written question or a video and ask for a solution.
Ability to access any of the 4 Quadrants (as listed above) to ask for an expert, via experience, advice and wisdom from those who have similar challenges.

```html
<!DOCTYPE html>
<html lang="en">
<head>
<meta charset="utf-8">
<title>WeatheredIt.net</title>
<link href="https://fonts.googleapis.com/css2?family=Ubuntu:wght@300;400;500;700&family=Arimo:ital,wght@0,400;0,700;1,400;1,700&display=swap" rel="stylesheet">
<style>
:root{
  --orange:#f26a12;
  --orange-deep:#e8520c;
  --orange-light:#ff9a1e;
  --yellow:#ffe21a;
  --ink:#2b2b2b;
  --text:#444;
  --muted:#777;
  --page:#e5e5e5;
  --panel:#f4f4f4;
  --white:#fff;
  --footer:#2c2c2c;
}
*{box-sizing:border-box;margin:0;padding:0}
html,body{width:874px;height:1200px;overflow:hidden}
body{position:relative;background:var(--page);font-family:Arimo,Arial,sans-serif;color:var(--text)}
.abs{position:absolute}

/* header */
.header{left:0;top:0;width:874px;height:102px;background:linear-gradient(#fff,#f2f2f2)}
.brand{left:80px;top:22px;display:flex;align-items:center;gap:10px}
.brand-mark{width:52px;height:52px;background:var(--orange);border-radius:6px}
.brand-name{font-family:Ubuntu,sans-serif;font-weight:700;font-size:24px;color:var(--orange)}
.brand-tag{left:142px;top:72px;font-family:Ubuntu,sans-serif;font-size:9px;color:var(--muted);font-weight:500}
.follow{font-family:Ubuntu,sans-serif;font-weight:700;font-size:10px;color:#777}
.social{display:flex;gap:6px}
.social span{width:24px;height:24px;border-radius:50%;background:radial-gradient(circle at 40% 35%,#eee,#888);border:2px solid #ddd;display:flex;align-items:center;justify-content:center}
.nav{left:333px;top:64px;height:24px;display:flex;align-items:center;font-family:Ubuntu,sans-serif;font-size:11px;color:var(--ink)}
.nav a{color:inherit;text-decoration:none}
.nav .home{width:67px;height:24px;background:linear-gradient(var(--orange-light),var(--orange));color:#fff;border-radius:2px;display:flex;align-items:center;justify-content:center;box-shadow:0 1px 2px rgba(0,0,0,.3)}
.dropdown{left:483px;top:90px;width:133px;font-family:Ubuntu,sans-serif;font-size:10px;background:#f5ecea;box-shadow:0 2px 5px rgba(0,0,0,.35);z-index:5}
.dropdown div{height:23px;line-height:23px;padding-left:9px;border-bottom:1px solid #ddd;color:var(--ink)}
.dropdown .active{background:linear-gradient(#555,#2b2b2b);color:#fff}

/* hero */
.hero{left:0;top:102px;width:874px;height:384px;background:radial-gradient(ellipse at 65% 60%,#ff9a22 0%,#f7761a 45%,#ee5a16 100%)}
.notch{left:0;top:462px}
.paper-back{left:86px;top:128px;width:330px;height:325px;background:#f5f5f5;transform:rotate(-5deg);box-shadow:0 2px 6px rgba(0,0,0,.3)}
.frame{left:99px;top:142px;width:301px;height:300px;background:#fff;box-shadow:0 3px 8px rgba(0,0,0,.35)}
.photo{left:109px;top:150px;width:284px;height:283px;background:linear-gradient(160deg,#6a6a6a,#3e3e3e 55%,#2a2a2a)}
.ribbon{left:76px;top:164px;width:160px;height:22px;background:linear-gradient(#ff9b1c,#f07a0f);transform:rotate(-45deg);transform-origin:center;color:#fff;font-family:Ubuntu,sans-serif;font-weight:700;font-size:12px;text-align:center;line-height:22px;box-shadow:0 2px 3px rgba(0,0,0,.3)}
.hero-q{left:436px;top:140px;font-family:Ubuntu,sans-serif;font-weight:700;font-size:52px;color:var(--yellow);text-shadow:0 2px 2px rgba(160,60,0,.5)}
.hero-h{left:436px;top:206px;font-family:Ubuntu,sans-serif;font-weight:700;font-size:42px;line-height:46px;color:#fff}
.hero-p{left:434px;top:310px;width:360px;font-size:11px;line-height:14px;color:#fff}
.more{left:634px;top:389px;width:124px;height:33px;background:linear-gradient(#fff,#e9e9e9);border-radius:4px;color:var(--orange-deep);font-family:Ubuntu,sans-serif;font-weight:700;font-size:15px;display:flex;align-items:center;justify-content:center;box-shadow:0 2px 3px rgba(0,0,0,.3)}

/* overview */
.sec-icon{width:40px;height:42px;background:var(--orange);border-radius:3px}
.sec-title{font-family:Ubuntu,sans-serif;font-weight:700;font-size:17px;color:var(--orange)}
.copy{font-size:9.4px;line-height:15.2px;color:var(--text);text-align:justify}
.readmore{left:470px;top:682px;width:63px;height:25px;border-radius:5px;background:linear-gradient(#999,#6c6c6c);color:#fff;font-size:8.5px;font-weight:700;font-style:italic;display:flex;align-items:center;justify-content:center}

/* quadrant cards */
.card{width:231px;height:148px;background:var(--panel);box-shadow:0 0 3px rgba(0,0,0,.12)}
.card .art{position:absolute;left:8px;top:6px;width:80px;height:78px;border-radius:6px}
.card h3{position:absolute;left:104px;top:22px;font-family:Ubuntu,sans-serif;font-weight:300;font-size:21px;line-height:23px;color:#333;letter-spacing:.5px}
.card h3 span{color:var(--orange)}
.card p{position:absolute;left:10px;bottom:14px;width:212px;font-size:9.4px;line-height:13.6px;text-align:justify;color:var(--text)}

/* form */
.form{left:578px;top:541px;width:232px;height:333px;background:var(--white);box-shadow:0 0 3px rgba(0,0,0,.12)}
.field{position:absolute;background:linear-gradient(#fff,#f6f6f6);border:1px solid #ddd;border-radius:10px;font-size:9.4px;color:#333;padding:8px 8px}
.btn-browse{background:linear-gradient(#eee,#c9c9c9);font-size:9.4px;font-weight:700;color:#333;display:flex;align-items:center;justify-content:center}
.btn-submit{background:linear-gradient(var(--orange-light),var(--orange-deep));border-radius:6px;color:#fff;font-family:Ubuntu,sans-serif;font-weight:700;font-size:11px;display:flex;align-items:center;justify-content:center}

/* video */
.video{left:589px;top:925px;width:209px;height:149px;background:#111;padding:4px}
.video .still{width:201px;height:130px;background:radial-gradient(circle at 50% 55%,#b3a0ff,#6a4bd6 35%,#2b1a6a 75%,#140c35)}

/* footer */
.footer{left:0;top:1089px;width:874px;height:111px;background:var(--footer)}
.foot-brand{left:70px;top:1122px;display:flex;align-items:center;gap:8px}
.foot-brand .mark{width:40px;height:40px;background:#6a6a6a;border-radius:4px}
.foot-brand .name{font-family:Ubuntu,sans-serif;font-weight:700;font-size:17px;color:#8a8a8a}
.foot-nav{left:259px;top:1126px;font-size:9.4px;color:#cfcfcf;display:flex;gap:12px}
.foot-copy{left:276px;top:1144px;font-size:9.4px;color:#cfcfcf}
.foot-social{left:672px;top:1139px;display:flex;gap:4px}
.foot-social span{width:30px;height:30px;border-radius:50%;background:radial-gradient(circle at 40% 35%,#ff9a4a,#e5480f);border:2px solid #eee}
</style>
</head>
<body>

<header class="abs header"></header>
<div class="abs brand"><span class="brand-mark"></span><span class="brand-name">WeatheredIt.net</span></div>
<div class="abs brand-tag">wisdom from all of us</div>
<div class="abs follow" style="left:723px;top:9px">Follow Us on:</div>
<div class="abs social" style="left:680px;top:28px">
  <span></span><span></span><span></span>
  <span><svg width="12" height="9" viewBox="0 0 12 9"><rect x=".5" y=".5" width="11" height="8" fill="none" stroke="#fff"/><path d="M.5 .5 6 5 11.5 .5" fill="none" stroke="#fff"/></svg></span>
</div>
<nav class="abs nav">
  <a class="home">Home</a>
  <span style="margin:0 28px 0 6px">|</span><a>About Us</a>
  <span style="margin:0 28px 0 24px">|</span><a>Support</a>
  <span style="margin:0 28px 0 27px">|</span><a>Share Problems</a>
  <span style="margin:0 28px 0 26px">|</span><a>Contact</a>
</nav>

<section class="abs hero"></section>
<svg class="abs notch" width="874" height="26" viewBox="0 0 874 26"><path d="M0 24H366C380 24 384 2 398 2H466C480 2 484 24 498 24H874V26H0Z" fill="var(--page)"/><path d="M0 24H366C380 24 384 2 398 2H466C480 2 484 24 498 24H874" fill="none" stroke="#fff" stroke-width="2"/></svg>
<div class="abs paper-back"></div>
<div class="abs frame"></div>
<div class="abs photo" role="img" aria-label="Photo of a distressed man sitting on stone steps holding his head"></div>
<div class="abs ribbon">Financial Problem</div>
<div class="abs hero-q">Problems ?</div>
<h1 class="abs hero-h">Share them all,<br>to RESOLVE it !!</h1>
<p class="abs hero-p">Vivamus lobortis velit sit amet ante ornare ornare sed vitae neque. Sed blandit pharetra mollis. Aliquam erat volutpat. Etiam ullamcorper ipsum non sapien varius aliquam. Duis feugiat semper commodo. Curabitur pulvinar augue sed erat feugiat at interdum dui molestie.</p>
<div class="abs more">More Details..</div>

<div class="abs dropdown">
  <div class="active">Financial</div><div>Medical &amp; Physical</div><div>Legal Matters</div><div>Psychological &amp; Spiritual</div>
</div>

<div class="abs sec-icon" style="left:61px;top:498px"></div>
<h2 class="abs sec-title" style="left:112px;top:510px">Overview</h2>
<p class="abs copy" style="left:61px;top:548px;width:473px"><b><i>Lorem ipsum dolor sit amet, consectetur adipiscing elit. Nulla ac dolor quis leo blandit bibendum.</i></b> Pellentesque malesuada leo non nunc placerat eu vehicula ante lacinia. Quisque tempus laoreet lacus, at semper dolor tempus vel. Aliquam pretium laoreet mattis. Cras eu ipsum magna, ut consequat nulla. Donec semper tortor at magna egestas mollis fringilla nisi bibendum. Aliquam vel posuere lorem. Pellentesque leo est, placerat ut molestie a, euismod ac turpis. Curabitur vehicula mi at neque ultrices sed suscipit erat condimentum.</p>
<p class="abs copy" style="left:61px;top:639px;width:473px">Pellentesque habitant morbi tristique senectus et netus et malesuada fames ac turpis egestas. Phasellus dolor ipsum, varius sed rhoncus sed, lobortis at justo. Vestibulum ante ipsum primis in faucibus orci luctus et ultrices posuere cubilia Curae...</p>
<div class="abs readmore">Read more..</div>

<article class="abs card" style="left:61px;top:758px">
  <div class="art" role="img" aria-label="Illustration of banknotes and gold coins" style="background:linear-gradient(135deg,#d9d9c8,#b9a65a)"></div>
  <h3><span>FINANCIAL</span><br>PROBLEMS</h3>
  <p>Donec semper tortor at magna egestas mollis fringilla nisi bibendum. Aliquam vel posuere lorem. Pellentesque leo est...</p>
</article>
<article class="abs card" style="left:315px;top:758px">
  <div class="art" role="img" aria-label="Illustration of a nurse figure with a kidney diagram" style="background:linear-gradient(135deg,#f3d6b8,#c9d9ee)"></div>
  <h3 style="left:106px;top:20px"><span>MEDICAL &amp;</span><br>PHYSICAL</h3>
  <p>Donec semper tortor at magna egestas mollis fringilla nisi bibendum. Aliquam vel posuere lorem. Pellentesque leo est...</p>
</article>
<article class="abs card" style="left:61px;top:932px">
  <div class="art" role="img" aria-label="Illustration of a wooden judge's gavel" style="background:linear-gradient(135deg,#d8a86a,#8a4e1c)"></div>
  <h3><span>LEGAL</span><br>MATTERS</h3>
  <p>Donec semper tortor at magna egestas mollis fringilla nisi bibendum. Aliquam vel posuere lorem. Pellentesque leo est...</p>
</article>
<article class="abs card" style="left:315px;top:932px">
  <div class="art" role="img" aria-label="Illustration of a water drop inside a circle" style="left:6px;width:62px;height:62px;top:10px;border-radius:50%;background:radial-gradient(circle,#9a9a9a,#555)"></div>
  <h3 style="left:69px"><span>SPIRITUAL &amp;</span><br>PSYCOLOGICAL</h3>
  <p>Donec semper tortor at magna egestas mollis fringilla nisi bibendum. Aliquam vel posuere lorem. Pellentesque leo est...</p>
</article>

<div class="abs" role="img" aria-label="Notebook and pen icon" style="left:582px;top:504px;width:28px;height:28px;background:linear-gradient(135deg,#9a4a22,#4a2010);border-radius:3px"></div>
<h2 class="abs sec-title" style="left:618px;top:507px">Post your Challange</h2>
<form class="abs form">
  <p style="position:absolute;left:17px;top:10px;width:200px;font-size:9.4px;line-height:13.6px;text-align:justify">Pellentesque leo est, placerat ut molestie a, euismod ac turpis.</p>
  <div class="field" style="left:16px;top:45px;width:197px;height:27px">Your Name</div>
  <div class="field" style="left:16px;top:80px;width:197px;height:27px">Your Email</div>
  <div class="field" style="left:16px;top:115px;width:197px;height:102px">Your Challange</div>
  <div style="position:absolute;left:102px;top:219px;font-size:15px;font-style:italic;color:#333">or</div>
  <div class="field" style="left:16px;top:245px;width:121px;height:27px">Post your Video</div>
  <div class="abs btn-browse" style="left:147px;top:248px;width:57px;height:21px">Browse</div>
  <div class="abs btn-submit" style="left:18px;top:289px;width:66px;height:25px">Submit</div>
</form>

<div class="abs" role="img" aria-label="Film reel icon" style="left:594px;top:888px;width:30px;height:30px;border-radius:50%;background:radial-gradient(circle,#ddd,#555)"></div>
<h2 class="abs sec-title" style="left:634px;top:893px">Recent Videos</h2>
<div class="abs video">
  <div class="still" role="img" aria-label="Video still of a meditating figure in glowing purple light"></div>
  <svg style="position:absolute;left:82px;top:52px" width="40" height="40" viewBox="0 0 40 40"><circle cx="20" cy="20" r="18" fill="rgba(255,255,255,.25)" stroke="rgba(255,255,255,.6)" stroke-width="2"/><path d="M15 11 29 20 15 29Z" fill="rgba(255,255,255,.75)"/></svg>
  <svg style="position:absolute;left:4px;top:136px" width="201" height="10" viewBox="0 0 201 10"><path d="M3 2 8 5 3 8Z" fill="#fff"/><rect x="14" y="4" width="120" height="2" fill="#666"/><rect x="170" y="3" width="20" height="4" fill="#888"/></svg>
</div>

<footer class="abs footer"></footer>
<div class="abs foot-brand"><span class="mark"></span><span class="name">WeatheredIt.net</span></div>
<nav class="abs foot-nav"><span>Home</span><span>~</span><span>About Us</span><span>~</span><span>Support</span><span>~</span><span>Share Problems</span><span>~</span><span>Contact</span></nav>
<div class="abs foot-copy">Copyright WeatheredIt.net © 2012-13 | &nbsp;Privacy Policy &nbsp;| &nbsp;Terms of Use</div>
<div class="abs follow" style="left:738px;top:1120px;color:#ddd">Follow Us on:</div>
<div class="abs foot-social"><span></span><span></span><span></span><span></span></div>

</body>
</html>
```